Willow Harbor Family Relief-buis card/stationary design for our non profit company
Have fun, be creative and lets see what you come up with!
Willow Harbor Family Relief-buis card/stationary design for our non profit company - Health
Creative Brief
Bright & Fun-filled
Dana Holloway
27415 Marlow Ave Ste#208 Lakemont CA 94318
harborwr@brightpostmail.net
We have not yet decided our titles yet. In the meantime please focus on the design. Once we choose the design we want, we will ask you to put our names,title etc. Thank you!
Please put our tagline: "Bringing rest to those who give care" on the back of the card.

```html
<!DOCTYPE html>
<html lang="en">
<head>
<meta charset="utf-8">
<title>Willow Harbor Family Relief – Business Card</title>
<link href="https://fonts.googleapis.com/css2?family=Cinzel:wght@400;700&display=swap" rel="stylesheet">
<style>
  :root {
    --page: #ffffff;
    --navy: #0b2672;
    --deep: #12389a;
    --mid: #2a66c2;
    --sky: #4a9ce0;
    --white: #ffffff;
    --shadow: rgba(0, 0, 0, 0.28);
    --paper: #fbfbfb;
  }
  * { margin: 0; padding: 0; box-sizing: border-box; }
  html, body {
    width: 1200px; height: 362px; overflow: hidden;
    background: var(--page);
    font-family: "Cinzel", Georgia, serif;
  }
  .canvas { position: relative; width: 1200px; height: 362px; }

  .card {
    position: absolute; top: 12px;
    width: 545px; height: 307px;
    box-shadow: 4px 8px 14px var(--shadow);
  }

  /* front */
  .card--front { left: 19px; background: var(--paper); padding: 17px 24px 19px 24px; }
  .front-field {
    width: 100%; height: 100%;
    background: radial-gradient(ellipse 55% 70% at 48% 48%, var(--mid) 0%, var(--deep) 55%, var(--navy) 100%);
    display: flex; align-items: center; justify-content: center; gap: 16px;
  }
  .front-mark {
    width: 34px; height: 34px; border-radius: 50%;
    background: var(--white);
  }
  .front-name {
    color: var(--white); font-weight: 700;
    font-size: 26px; line-height: 1.15; letter-spacing: 1px;
    text-transform: uppercase;
  }

  /* back */
  .card--back {
    left: 636px; color: var(--white);
    background: linear-gradient(90deg, var(--sky) 0%, var(--mid) 30%, var(--deep) 60%, var(--navy) 100%);
  }
  .brand { position: absolute; left: 270px; top: 58px; display: flex; align-items: center; gap: 8px; }
  .brand-dot { width: 26px; height: 26px; border-radius: 50%; background: var(--white); }
  .brand-name {
    font-weight: 700; font-size: 13px; line-height: 1.05;
    text-transform: uppercase; letter-spacing: 0.3px;
  }
  .tagline {
    position: absolute; left: 270px; top: 95px;
    font-size: 7.5px; letter-spacing: 0.4px;
  }
  .contact { position: absolute; left: 295px; top: 150px; }
  .person {
    font-size: 15px; letter-spacing: 2.5px; margin-bottom: 14px;
  }
  .contact-line { font-size: 9px; letter-spacing: 0.6px; line-height: 14px; }
  .contact-line--gap { margin-top: 6px; }
</style>
</head>
<body>
<div class="canvas">

  <section class="card card--front">
    <div class="front-field">
      <span class="front-mark"></span>
      <span class="front-name">Willow Harbor<br>Family Relief</span>
    </div>
  </section>

  <section class="card card--back">
    <div class="brand">
      <span class="brand-dot"></span>
      <span class="brand-name">Willow Harbor<br>Family Relief</span>
    </div>
    <p class="tagline">Bringing rest to those who give care</p>

    <div class="contact">
      <p class="person">Dana Holloway</p>
      <p class="contact-line">27415 Marlow Ave Ste#208</p>
      <p class="contact-line">Lakemont CA 94318</p>
      <p class="contact-line contact-line--gap">harborwr@brightpostmail.net</p>
      <p class="contact-line contact-line--gap">1(800)555-0142</p>
    </div>
  </section>

</div>
</body>
</html>
```